Wrenfield food and drinks menu

Tamarind on Vellory is a vegan restaurant in NYC. It's food menu is given to guests on a casual clipboard, on regular sized 8.5 x 11 sheets of paper.

The assignment is to create a drinks menu to make the cocktail, wine and beer offerings more prominent. The drinks menu should be half the size of the regular menu so it sits smaller on top of the 8.5 x 11 sheet of paper. Other requirements:

-Please refer to the website design for inspiration and style guide
wrenfieldeats.com
-brand assets, the logo for Tamarind on Vellory and color treatments are here
https://www.filecrate.example/sh/8kqpwz2lmtdfa/QXvbnPzr4T
- if there is too much copy the drinks menu can be laid out on a 8.5 x 11 sheet of paper that opens like a book horizontally, with a front cover, then the inside left and right panels and back panel can have text.

The drinks menu should be organized by:

Organic Cocktails
Wines by the glass (white, red, rose)
Sparkling
Beer
Non alcoholic

List of drinks are enclosed

Industry/Entity Type

Restaurant

Requirements
Must have
• Tamarind on Vellory logo, and all the drink items listed in the attached menu.
Use fonts that are in the brand asset dropbox.
Should not have
• Lots of color. This will most likely not be printed in color.

```html
<!DOCTYPE html>
<html lang="en">
<head>
<meta charset="utf-8">
<title>Wrenfield food and drinks menu</title>
<link rel="stylesheet" href="https://fonts.googleapis.com/css2?family=Open+Sans:ital,wght@0,400;0,600;1,400&display=swap">
<style>
  :root {
    --page: #ffffff;
    --paper: #f3efe7;
    --ink: #5a5a55;
    --heading: #5b6b5e;
    --forest: #4a6350;
    --mustard: #cfc421;
    --leaf: #8fae3c;
    --logo-green: #4f6b3c;
  }
  * { margin: 0; padding: 0; box-sizing: border-box; }
  html, body { width: 1200px; height: 311px; overflow: hidden; background: var(--page); }
  body { position: relative; font-family: "Open Sans", Arial, sans-serif; color: var(--ink); }
  .top-rule { position: absolute; left: 0; top: 0; width: 1200px; height: 1px; background: #cfcfcf; }

  .section-title {
    position: absolute; font-size: 13px; color: var(--heading); text-align: center; white-space: nowrap;
  }
  .section-title.cover { left: 245px; width: 150px; top: 38px; }
  .section-title.inside { left: 780px; width: 250px; top: 35px; }

  .panel { position: absolute; background: var(--paper); overflow: hidden; }
  .cover-front { left: 45px; top: 68px; width: 275px; height: 210px; }
  .cover-back { left: 325px; top: 68px; width: 275px; height: 210px; }
  .food { left: 632px; top: 66px; width: 275px; height: 212px; }
  .drinks { left: 912px; top: 66px; width: 275px; height: 212px; }

  .brand-name {
    position: absolute; left: 0; width: 100%; top: 100px; text-align: center;
    font-size: 10px; font-weight: 600; letter-spacing: 0.5px; color: var(--logo-green);
  }

  .accent-rule { position: absolute; left: 0; top: 13px; width: 100%; height: 2px; background: var(--mustard); }
  .footer-band { position: absolute; left: 0; bottom: 0; width: 100%; height: 16px; background: var(--forest); }
  .footer-dot { position: absolute; left: 8px; top: 4px; width: 8px; height: 8px; border-radius: 50%; background: var(--paper); opacity: 0.8; }
  .footer-name { position: absolute; right: 6px; top: 3px; font-size: 8px; font-weight: 600; letter-spacing: 0.6px; color: var(--paper); }

  .menu-text { position: absolute; left: 0; width: 100%; text-align: center; font-size: 3.9px; line-height: 5px; }
  .menu-heading { font-weight: 600; font-size: 4.6px; color: #4f4f4a; }
  .menu-item { display: block; }

  .large-plates-heading { top: 23px; }
  .large-plates { top: 36px; }
  .large-plates .menu-item { margin-bottom: 5.4px; }
  .sweets-heading { top: 118px; }
  .sweets { top: 133px; }
  .sweets .menu-item { margin-bottom: 5.4px; }

  .drinks-heading { top: 23px; }
  .drink-list { top: 36px; line-height: 5.6px; }
  .chef { top: 88px; }
  .dots { position: absolute; left: 0; width: 100%; top: 103px; height: 9px; display: flex; justify-content: center; gap: 11px; }
  .dot { width: 8px; height: 8px; border-radius: 50%; }
  .dot.forest { background: var(--forest); }
  .dot.mustard { background: var(--mustard); }
  .dot.leaf { background: var(--leaf); }
  .diet-key { top: 122px; }
  .gratuity { top: 136px; }
  .sourcing { top: 149px; line-height: 6.5px; }
  .thanks { top: 176px; font-size: 6.6px; font-style: italic; line-height: 8px; }
</style>
</head>
<body>
  <div class="top-rule"></div>

  <div class="section-title cover">cover menu</div>
  <div class="section-title inside">food menu and drink menu</div>

  <section class="panel cover-front">
    <div class="brand-name">Tamarind on Vellory</div>
  </section>
  <section class="panel cover-back"></section>

  <section class="panel food">
    <div class="accent-rule"></div>
    <div class="menu-text menu-heading large-plates-heading">Large plates</div>
    <div class="menu-text large-plates">
      <span class="menu-item">sliders ~ seitan /mushroom patty, poblano 1000 island,fried onion, lettuce, tomato, pickle,<br>served with your choice of field greens or french fries ~ 14 (nf)</span>
      <span class="menu-item">pasta ~ elbow macaroni, artichoke hearts, english peas, truffled cashew cream, mint pesto ~ 16</span>
      <span class="menu-item">pizza ~ plum tomato ragout, cashew ricotta, mozzarella, smoked fennel, pesto, arugula ~ 14</span>
      <span class="menu-item">tagine ~ orange scented millet, chickpeas, dried apricots, oil cured olives, moroccan spiced tomato broth ~ 17 (gf, nf, sf)</span>
      <span class="menu-item">piccata ~ pan seared seitan cutlets, lemon/white wine butter, fried capers ~ 19</span>
      <span class="menu-item">marsala ~ pan seared seitan cutlets, spicy marsala pan sauce, fingerling as rattr potatoes, sautéed kale ~ 19</span>
    </div>
    <div class="menu-text menu-heading sweets-heading">sweets</div>
    <div class="menu-text sweets">
      <span class="menu-item">chocolate truffles "of the moment" ~ 10</span>
      <span class="menu-item">strawberry short cake, fresh crème and strawberries, vanilla ice cream ~ 10 (nf)</span>
      <span class="menu-item">peach and strawberry crumble, vanilla ice cream ~ 9 (nf)</span>
      <span class="menu-item">new york cheesecake, peach reduction, chocolate chips ~ 11 (nf)</span>
      <span class="menu-item">blueberry bread pudding, vanilla glaze, fresh blueberries ~ 9 (nf)</span>
    </div>
    <div class="footer-band"><div class="footer-dot"></div></div>
  </section>

  <section class="panel drinks">
    <div class="accent-rule"></div>
    <div class="menu-text menu-heading drinks-heading">Drinks</div>
    <div class="menu-text drink-list">
      Organic Cocktails<br>Wines by the glass (white, red, rose)<br>Sparkling<br>Beer<br>Non alcoholic
    </div>
    <div class="menu-text chef">executive chef : Marcus Delane</div>
    <div class="dots">
      <span class="dot forest"></span><span class="dot mustard"></span><span class="dot leaf"></span>
    </div>
    <div class="menu-text diet-key">gf = gluten free, nf = nut free, sf = soy free</div>
    <div class="menu-text gratuity">a 20% gratuity is applied to parties of five or more</div>
    <div class="menu-text sourcing">all of our offerings are completely free of any animal products<br>and ar organic and/or local as possible</div>
    <div class="menu-text thanks">thanks for dining with us!</div>
    <div class="footer-band"><div class="footer-name">WRENFIELD</div></div>
  </section>
</body>
</html>
```